Client Proposal

I need a proposal template to give to potential clients detailing our services, safety, company history, table of contents and appendixes. I need a cover page to start with images describing our services. Our company is based in Grande Prairie, Alberta. We do land survey work, engineering and environmental.

In word format please so that we can change the proposal on an as needed basis.

```html
<!DOCTYPE html>
<html lang="en">
<head>
<meta charset="utf-8">
<title>Our Service – Northbound Group</title>
<link rel="stylesheet" href="https://fonts.googleapis.com/css2?family=Roboto:wght@400;500;700;900&display=swap">
<style>
  :root {
    --navy: #1b2a5c;
    --navy-deep: #142150;
    --teal: #2a7f9a;
    --sky: #cfe4fa;
    --sky-light: #e9f3fd;
    --ink: #1c1c1c;
    --white: #ffffff;
    --scene-top: #a9bfa6;
    --scene-bottom: #d9a887;
  }
  * { margin: 0; padding: 0; box-sizing: border-box; }
  html, body { width: 1200px; height: 685px; overflow: hidden; }
  body { font-family: "Roboto", Arial, sans-serif; color: var(--ink); }

  .canvas {
    position: relative;
    width: 1200px;
    height: 685px;
    overflow: hidden;
    background: radial-gradient(circle at 900px 320px, var(--white) 0, var(--sky-light) 170px, var(--sky) 430px);
  }

  .header-band {
    position: absolute;
    left: 0; top: 0;
    width: 1200px; height: 128px;
    background: linear-gradient(100deg, var(--navy-deep) 0%, var(--navy) 55%, #1e3a6e 100%);
  }
  .header-band svg { position: absolute; inset: 0; }

  .page-title {
    position: absolute;
    left: 109px; top: 64px;
    font-size: 38px; font-weight: 900;
    line-height: 1;
    color: var(--white);
    letter-spacing: 0.3px;
  }

  .brand {
    position: absolute;
    left: 762px; top: 52px;
    display: flex; align-items: center; gap: 12px;
  }
  .brand-mark { width: 30px; height: 30px; background: var(--white); }
  .brand-name {
    font-size: 24px; font-weight: 700;
    color: var(--white);
    letter-spacing: 1px;
    text-transform: uppercase;
  }

  .column-head {
    position: absolute;
    top: 159px; height: 31px; width: 311px;
    background: var(--navy);
    color: var(--white);
    font-size: 20px; font-weight: 700;
    display: flex; align-items: center;
    padding-left: 16px;
    white-space: nowrap;
  }
  .column-head.construction { left: 114px; }
  .column-head.services { left: 444px; justify-content: center; padding-left: 0; }
  .column-head.environmental { left: 771px; padding-left: 13px; }

  .construction-list {
    position: absolute;
    left: 133px; top: 210px;
    list-style: none;
    font-size: 16px; line-height: 25.4px;
    white-space: nowrap;
  }
  .construction-list li { margin-bottom: 25.4px; }
  .construction-list strong { font-weight: 700; display: block; }
  .construction-list strong::before { content: "• "; }

  .bullet-list {
    position: absolute;
    list-style: none;
    font-size: 16px; line-height: 25.4px;
    white-space: nowrap;
  }
  .bullet-list li::before { content: "• "; }
  .bullet-list.services { left: 486px; top: 207px; }
  .bullet-list.environmental { left: 820px; top: 210px; }

  .services-visual {
    position: absolute;
    left: 505px; top: 425px;
    width: 695px; height: 260px;
    border-top-left-radius: 24px;
    background: linear-gradient(180deg, var(--scene-top) 0%, var(--scene-bottom) 100%);
  }
</style>
</head>
<body>
<main class="canvas">
  <header class="header-band">
    <svg width="1200" height="128" aria-hidden="true">
      <polygon points="34,30 68,48 34,66" fill="#2a7f9a" opacity="0.7"/>
      <polygon points="160,10 205,30 160,50" fill="#2a7f9a" opacity="0.55"/>
      <polygon points="66,100 84,110 66,120" fill="#2a7f9a" opacity="0.6"/>
      <polygon points="530,72 552,84 530,96" fill="#2a7f9a" opacity="0.7"/>
      <polygon points="615,12 640,25 615,38" fill="#2a7f9a" opacity="0.7"/>
    </svg>
    <h1 class="page-title">OUR SERVICE</h1>
    <div class="brand">
      <span class="brand-mark"></span>
      <span class="brand-name">Northbound Group</span>
    </div>
  </header>

  <h2 class="column-head construction">CONSTRUCTION SERVICES</h2>
  <h2 class="column-head services">SERVICES</h2>
  <h2 class="column-head environmental">ENVIRONMENTAL SERVICES</h2>

  <ul class="construction-list">
    <li><strong>3D Machine Control:</strong>Training/Support, 3D Data Preparation<br>and Modeling, Quantity Takeoffs/<br>Volumetric Supervision</li>
    <li><strong>Construction Surveying:</strong>Pile/Grid Line Layout, Building<br>Services, As-built Surveys, Volumetric<br>Surveys, Highway Layout,<br>Topographic Surveys</li>
    <li><strong>Consulting Services:</strong>Machine Control Implementation and<br>Integration, Survey Technology and<br>3D Machine Control Applications in<br>Industry</li>
  </ul>

  <ul class="bullet-list services">
    <li>Civil Design</li>
    <li>Civil Survey Support</li>
    <li>3D Machine Control Support</li>
    <li>Pile Layout</li>
    <li>Cap Alignments</li>
    <li>Anchor Bolt Layout</li>
    <li>Precision Surveys</li>
    <li>Laser Scanning</li>
  </ul>

  <ul class="bullet-list environmental">
    <li>Flow Rate Measurements</li>
    <li>Wetlands Assessments</li>
    <li>Code of Practice</li>
    <li>Wildlife Sweeps</li>
    <li>Presite Assessments</li>
  </ul>

  <div class="services-visual" role="img" aria-label="Photo montage: an open hand holding a tablet with an excavator, pine tree, hard hat, survey instrument on tripod, rolled blueprints and a terrain model"></div>
</main>
</body>
</html>
```